Web Design Project

Revamp current website adding newly designed logo and creating layout that is good on desktops, tablets, and cell phones.

Current website can be viewed at www.venkirainteriors.com

Will you see the website is small but graphics heavy in the gallery. The gallery needs to be setup so that it is easy to maintain the links and update the photos.

Needs to have high visual impact.

I need a new logo and website layout designed for my partner's business. This is a birthday present. His business is interior painting, wallpapering and design. He also has access to a wide variety of products including carpet, fabrics, furniture, wallpaper, tile, countertops, etc. I have attached some screen shots of his website for reference. He is a one man shop and has a stellar reputation with his customers. He is on-time, very tidy, excellent with animals, and always finishes on time and on budget. There are no restrictions on colors or fonts. The logo needs to work well with the website, business cards and printed materials. The website needs to flow content for device size so it looks just as good on a cell phone or tablet as it does on a desktop computer. Whatever the heck that's called! Thanks. I am looking forward to seeing everyone's ideas.

Target Market(s)

Consumers looking for interior design, painting, and wallpapering as well as interior products such as flooring, window treatments, reupholstering, counter tops, etc.

Industry/Entity Type

Cell Phone

Requirements
Must have
• Clean, sharp, visual impact (at least on the home page)
Should not have
• Clutter.

```html
<!DOCTYPE html>
<html lang="en">
<head>
<meta charset="utf-8">
<title>Venkira Interior Designs</title>
<link href="https://fonts.googleapis.com/css2?family=Jost:wght@400&family=Great+Vibes&display=swap" rel="stylesheet">
<style>
  :root {
    --wine: #7d1119;
    --wine-dark: #6a0c13;
    --wine-light: #9a1a22;
    --ink: #111111;
    --muted: #4a4a4a;
    --rule: #cfcfcf;
    --bg-light: #fbfbfb;
    --bg-mid: #f1f1f1;
    --bg-edge: #e2e2e2;
    --arrow: #8a8a8a;
  }
  html, body {
    margin: 0;
    padding: 0;
    overflow: hidden;
  }
  .page {
    position: relative;
    width: 1200px;
    height: 1036px;
    overflow: hidden;
    background: radial-gradient(ellipse at 50% 45%, var(--bg-light) 0%, var(--bg-mid) 55%, var(--bg-edge) 100%);
    font-family: Arial, Helvetica, sans-serif;
    color: var(--ink);
  }
  .brand {
    position: absolute;
    top: 52px;
    left: 0;
    width: 1200px;
    margin: 0;
    display: flex;
    justify-content: center;
    align-items: center;
    gap: 14px;
    font-family: "Jost", sans-serif;
    font-weight: 400;
    font-size: 36px;
    letter-spacing: 1px;
    color: var(--wine);
  }
  .brand-mark {
    width: 14px;
    height: 14px;
    background: var(--wine);
  }
  .main-nav {
    position: absolute;
    top: 140px;
    left: 127px;
    width: 942px;
    height: 36px;
    border-bottom: 1px solid var(--rule);
  }
  .main-nav a {
    position: absolute;
    top: 0;
    height: 36px;
    line-height: 36px;
    font-family: "Jost", sans-serif;
    font-size: 16px;
    color: var(--ink);
    text-decoration: none;
    text-transform: uppercase;
    white-space: nowrap;
  }
  .main-nav a.is-active {
    background: linear-gradient(var(--wine-light), var(--wine-dark));
    color: #ffffff;
    border-radius: 4px 4px 0 0;
    width: 79px;
    text-align: center;
  }
  .carousel-slide {
    position: absolute;
    box-shadow: 0 0 0 1px #ffffff;
  }
  .slide-shadow {
    position: absolute;
    height: 10px;
    border-radius: 50%;
    background: radial-gradient(ellipse at center, rgba(0,0,0,0.28) 0%, rgba(0,0,0,0) 70%);
  }
  .carousel-arrow {
    position: absolute;
    width: 46px;
    height: 46px;
  }
  .welcome {
    position: absolute;
    top: 730px;
    left: 0;
    width: 1200px;
    margin: 0;
    text-align: center;
    font-family: "Great Vibes", cursive;
    font-weight: 400;
    font-size: 45px;
    color: var(--wine);
  }
  .intro {
    position: absolute;
    top: 815px;
    left: 125px;
    width: 950px;
    text-align: center;
    font-size: 13.75px;
    line-height: 22px;
  }
  .intro p {
    margin: 0 0 22px;
  }
  .footer {
    position: absolute;
    top: 981px;
    left: 95px;
    width: 999px;
    border-top: 1px solid var(--rule);
    font-size: 12px;
    color: var(--muted);
  }
  .footer .copyright {
    position: absolute;
    top: 18px;
    left: 14px;
  }
  .footer .contact-line {
    position: absolute;
    top: 18px;
    right: 28px;
  }
</style>
</head>
<body>
<div class="page">
  <h1 class="brand"><span class="brand-mark"></span><span class="brand-name">Venkira Interior Designs</span></h1>

  <nav class="main-nav">
    <a class="is-active" href="#" style="left:102px">Home</a>
    <a href="#" style="left:235px">About Us</a>
    <a href="#" style="left:373px">Contact</a>
    <a href="#" style="left:511px">Gallery</a>
    <a href="#" style="left:637px">Products</a>
    <a href="#" style="left:781px">Services</a>
  </nav>

  <section class="carousel">
    <div class="slide-shadow" style="left:135px; top:567px; width:110px;"></div>
    <div class="slide-shadow" style="left:264px; top:624px; width:175px;"></div>
    <div class="slide-shadow" style="left:459px; top:684px; width:260px;"></div>
    <div class="slide-shadow" style="left:738px; top:624px; width:175px;"></div>
    <div class="slide-shadow" style="left:930px; top:567px; width:110px;"></div>

    <div class="carousel-slide" role="img" aria-label="Woman with a mug standing by a bright window"
         style="left:125px; top:342px; width:128px; height:224px; background:linear-gradient(160deg,#efe6d4,#d8cdb8 60%,#bdb29c);"></div>
    <div class="carousel-slide" role="img" aria-label="Modern kitchen with red cabinets and steel range hood"
         style="left:254px; top:285px; width:194px; height:336px; background:linear-gradient(180deg,#cfd2d6 0%,#b9bcc0 30%,#7d1d1c 55%,#5a1412 80%,#1c1a1c 100%);"></div>
    <div class="carousel-slide" role="img" aria-label="Empty room with coffered ceiling, French doors and hardwood floor"
         style="left:449px; top:230px; width:278px; height:447px; background:linear-gradient(180deg,#ece6da 0%,#c9b898 30%,#b8a582 55%,#8a5a36 75%,#6e3f22 100%);"></div>
    <div class="carousel-slide" role="img" aria-label="Dining room with wooden table, chairs and chandelier"
         style="left:728px; top:286px; width:192px; height:335px; background:linear-gradient(180deg,#c9a871 0%,#b99257 40%,#9a4a22 65%,#c8c3b8 100%);"></div>
    <div class="carousel-slide" role="img" aria-label="Bright room with tall windows overlooking trees"
         style="left:920px; top:342px; width:131px; height:224px; background:linear-gradient(180deg,#e6eef2 0%,#b9cfd8 40%,#8fa878 65%,#d9d7d2 100%);"></div>

    <svg class="carousel-arrow" style="left:69px; top:407px;" viewBox="0 0 46 46" aria-label="Previous">
      <circle cx="23" cy="23" r="21.5" fill="#ffffff" stroke="#8a8a8a" stroke-width="2.5"/>
      <polyline points="26,15 18,23 26,31" fill="none" stroke="#8a8a8a" stroke-width="4" stroke-linecap="round" stroke-linejoin="round"/>
    </svg>
    <svg class="carousel-arrow" style="left:1071px; top:430px;" viewBox="0 0 46 46" aria-label="Next">
      <circle cx="23" cy="23" r="21.5" fill="#ffffff" stroke="#8a8a8a" stroke-width="2.5"/>
      <polyline points="20,15 28,23 20,31" fill="none" stroke="#8a8a8a" stroke-width="4" stroke-linecap="round" stroke-linejoin="round"/>
    </svg>
  </section>

  <h2 class="welcome">Welcome to Venkira Interior Designs.</h2>

  <section class="intro">
    <p>With the various materials, colors, and finishes available the choices today can be daunting. By listening to you, I am able to pick just the right color, the right fabric, or the right furniture for your projects. Whether you are starting with a small project or a large project, I am ready to bring your ideas to life. It doesn't take a big budget to achieve dramatic effects. A wonderful new look is within anyone's reach.</p>
    <p>My guidance with the selection of colors, fabrics, paint, wallpaper, and furniture, as well as the placement of items in a room, will help you achieve the results you desire – a beautiful home that is a joy to walk into and to show off!</p>
  </section>

  <footer class="footer">
    <span class="copyright">Copyright © Venkira Interior Designs. All rights reserved.</span>
    <span class="contact-line">2870 W Linden Ridge Rd. • Marlow Falls, KS 66900 • (555) 014-2297</span>
  </footer>
</div>
</body>
</html>
```